Venture Capital firm needs modern business cards

We are a Venture Capital firm within financial services/Asset management. The industry generally has basic business cards with black, blue and maybe green/yellow design elements.
Our firm has a four-colour swoosh logo. We are based in London and want to stand out, just a little bit!, from the crowd. Our company is called ROLK Investments and the 'C' stands for collaboration thus using artfolkhub is a natural portal for our business card design competition. Our logo came via artfolkhub too!
We use 'Venture Partner in Asset Management' as our tagline and this is Trademark registered. We operate in a conservative industry and we should not overstep our mark. The logo is colorful as it is and therefore the rest of the design should not be too fanciful.
The objective is twofold: make our logo element stick and memorable with our audience, whilst representing a conservative yet young image.
The Business Card obviously needs a field for Name, Surname, Job Title, Adress fields: Street, City, Postcode, Country, telefone and cell number, website address, etc.
We have uploaded the ai file. We trust that these are OK. If not, please advise.
Reason: We have have been busy with a client engagement. We will set the project as Guaranteed in return for the troubles we cause. Apologies for the confusion.
Thank you all for these great and creative design suggestions. The team is very happy with a number of your ideas! We will be in touch tomorrow to give individual feedback before the project closes on Friday. We look forward to working with some of you to narrow down your creations. Thank you, ROLK Investments team.
All,
Target Market(s)
Financial Services Professionals, Investors, Media, 35-70 years, mainly male, well educated
Industry/Entity Type
Conservative
Requirements
Must have
- We must make use of our logo and potential tagline 'Venture Partner in Asset Management' as we are establishing a new Brand and new company in the market.
We can use 'ROLK', 'ROLK Investments', and 'ROLK Investments'+tagline 'Venture Partner in Asset Management' or simply the four-colour swoosh plus the name of the company as part of the text. (see files)
All design elements are available in black or grey-scale if required. (grey scale swoosh attached).
Due to regulation we must have the following wording on the card in small print 'ROLK Investments is an Appointed Representative of Brambury Monetary Ventures Limited, which is authorised by the Pemberton Oversight Board'.
Nice to have
- We would consider designs that make use of different printing techniques such embossing/debossing, UV spot etc.
We attach our colour palette in the files section for your reference.
Should not have
- The font we use for our company name is 'EXO' so do not use a font style that clashes with the corporate fonts, please.
Do not use other design elements than the ones we provide in the file library as part of this project.

```html
<!DOCTYPE html>
<html lang="en">
<head>
<meta charset="utf-8">
<title>ROLK Investments – Business Card</title>
<link href="https://fonts.googleapis.com/css2?family=Exo+2:ital,wght@0,300;0,400;0,500;1,400&display=swap" rel="stylesheet">
<style>
  :root {
    --stage: #e9e6e3;
    --charcoal: #33393b;
    --paper: #ffffff;
    --ink: #3a3f42;
    --pink: #e0157a;
    --pin-blue: #1ea3dc;
    --soft-white: #f2f2f2;
    --band-1: #5d9e36;
    --band-2: #8cc63f;
    --band-3: #c5d43a;
    --band-4: #f2d01a;
    --band-5: #6a1d4e;
    --band-6: #e21f7d;
    --band-7: #a9d9e2;
    --band-8: #6cc3c4;
    --band-9: #1ea3dc;
  }
  * { box-sizing: border-box; margin: 0; padding: 0; }
  html, body { width: 1200px; height: 866px; overflow: hidden; }
  body {
    background: var(--stage);
    font-family: "Exo 2", sans-serif;
    color: var(--ink);
    position: relative;
  }
  .card {
    position: absolute;
    width: 540px;
    height: 308px;
    border-radius: 14px;
    overflow: hidden;
    box-shadow: 0 6px 18px rgba(0,0,0,0.18);
  }
  .card--back { left: 40px; top: 279px; background: var(--charcoal); }
  .card--front { left: 620px; top: 279px; background: var(--paper); }

  .back-mark {
    position: absolute; left: 0; top: 0; width: 100%; height: 100%;
    display: flex; align-items: center; justify-content: center; gap: 14px;
  }
  .back-mark__dot { width: 22px; height: 22px; border-radius: 50%; background: var(--pink); }
  .back-mark__name { font-size: 64px; font-weight: 400; color: var(--soft-white); letter-spacing: 2px; }

  .brand {
    position: absolute; left: 36px; top: 34px;
    display: flex; align-items: center; gap: 10px;
  }
  .brand__dot { width: 14px; height: 14px; border-radius: 50%; background: var(--pink); }
  .brand__name { font-size: 30px; font-weight: 500; color: var(--ink); letter-spacing: 0.5px; }

  .contacts {
    position: absolute; right: 30px; top: 30px;
    text-align: right; font-size: 14px; line-height: 17px; color: var(--ink);
  }
  .contacts li { list-style: none; display: flex; justify-content: flex-end; align-items: center; gap: 7px; }
  .contacts .gap { margin-top: 14px; }
  .contacts svg { width: 11px; height: 11px; flex: none; }

  .address {
    position: absolute; left: 30px; top: 128px;
    font-size: 14px; line-height: 17px; font-style: italic; color: var(--ink);
    display: flex; gap: 8px;
  }
  .address svg { width: 9px; height: 12px; margin-top: 2px; }

  .band {
    position: absolute; left: 0; top: 186px; width: 100%; height: 6px; display: flex;
  }
  .band span { flex: 1; }
  .band span:nth-child(1) { background: var(--band-1); }
  .band span:nth-child(2) { background: var(--band-2); }
  .band span:nth-child(3) { background: var(--band-3); }
  .band span:nth-child(4) { background: var(--band-4); }
  .band span:nth-child(5) { background: var(--band-5); }
  .band span:nth-child(6) { background: var(--band-6); }
  .band span:nth-child(7) { background: var(--band-7); }
  .band span:nth-child(8) { background: var(--band-8); }
  .band span:nth-child(9) { background: var(--band-9); }

  .footer {
    position: absolute; left: 0; top: 192px; width: 100%; height: 116px;
    background: var(--charcoal);
  }
  .person { position: absolute; right: 34px; top: 18px; text-align: right; }
  .person__name { font-size: 28px; font-weight: 300; color: var(--soft-white); line-height: 30px; }
  .person__role { font-size: 16px; font-weight: 300; color: var(--pink); line-height: 16px; margin-top: -2px; }
  .disclaimer {
    position: absolute; left: 12px; right: 12px; bottom: 10px;
    font-size: 7px; font-style: italic; color: #c9cccd; white-space: nowrap; letter-spacing: 0.1px;
  }
</style>
</head>
<body>

  <section class="card card--back" aria-label="Card back">
    <div class="back-mark">
      <span class="back-mark__dot"></span>
      <span class="back-mark__name">ROLK</span>
    </div>
  </section>

  <section class="card card--front" aria-label="Card front">
    <div class="brand">
      <span class="brand__dot"></span>
      <span class="brand__name">ROLK Investments</span>
    </div>

    <ul class="contacts">
      <li>+44 20 0000 0000
        <svg viewBox="0 0 12 12"><path fill="var(--pink)" d="M2.5 1l2 2-1 1.3c.6 1.5 1.8 2.7 3.2 3.2L8 6.5l2 2-1.2 1.8C4.7 10 1.9 7.2 1.7 2.3z"/></svg>
      </li>
      <li>+44 20 0000 0000
        <svg viewBox="0 0 12 12"><rect x="3" y="0.8" width="6" height="10.4" rx="1.2" fill="none" stroke="var(--pink)" stroke-width="1.3"/><circle cx="6" cy="9.3" r="0.7" fill="var(--pink)"/></svg>
      </li>
      <li class="gap">daniel.harper@rolk-invest.co
        <svg viewBox="0 0 12 12"><rect x="0.8" y="2.5" width="10.4" height="7" fill="var(--pink)"/><path d="M1 3l5 3.5L11 3" fill="none" stroke="#fff" stroke-width="1"/></svg>
      </li>
      <li>www.rolk-invest.co
        <svg viewBox="0 0 12 12"><circle cx="6" cy="6" r="5" fill="none" stroke="var(--pink)" stroke-width="1.2"/><ellipse cx="6" cy="6" rx="2.2" ry="5" fill="none" stroke="var(--pink)" stroke-width="1"/><path d="M1 6h10" stroke="var(--pink)" stroke-width="1"/></svg>
      </li>
    </ul>

    <div class="address">
      <svg viewBox="0 0 9 12"><path fill="var(--pin-blue)" d="M4.5 0A4.2 4.2 0 0 0 .3 4.2C.3 7.3 4.5 12 4.5 12s4.2-4.7 4.2-7.8A4.2 4.2 0 0 0 4.5 0zm0 5.8a1.6 1.6 0 1 1 0-3.2 1.6 1.6 0 0 1 0 3.2z"/></svg>
      <p>Adress line 1<br>Adress line 2</p>
    </div>

    <div class="band" aria-hidden="true">
      <span></span><span></span><span></span><span></span><span></span><span></span><span></span><span></span><span></span>
    </div>

    <div class="footer">
      <div class="person">
        <p class="person__name">Daniel Harper</p>
        <p class="person__role">manager</p>
      </div>
      <p class="disclaimer">ROLK Investments is an Appointed Representative of Brambury Monetary Ventures Limited, which is authorised by the Pemberton Oversight Board</p>
    </div>
  </section>

</body>
</html>
```